New Fun, Positive, energised looking Business Card Needed for High Achiever Coach

I am looking for a two sided full colour business card. I am self employed and have recently re branded my 1-2-1 work re-vitalising high achievers. My target client base for these cards is therefore high achievers - usually aged 40 -55, they are often entrepreneurs, CEO or work in banking and finance and 2/3 are male. I work with them on 90 day or 6 month coaching programs to help them live their success in a healthier, more sustainable and fulfiiled way. They pay for this privately so though they are corporate types the cards need not look 'corporate'. I want to portray the idea of transformation, vitality and re-connecting.
You can get a feel for the look I like on my new website: corinvale.co.uk
I want to use this logo with strapline (Re-Vitalising High Achievers) (I purchased off Logoharbor) and font/ colours (the turquoise and green).
Details to include on the card:
www.corinvale.co.uk
+44 7915 264318
mira@corinvale.co.uk
skype: miracorin
I'd also like to include:
Do you struggle to switch off? Want to be healthier and feel fitter? Want closer relationships? More clarity over the direction you are headed? I can help you do these things using integrated mind-body techniques. Visit corinvale.co.uk TODAY to apply for a FREE Breakthrough session.
BUT if that is too much text for a card I am open to advice/ammendments.
Updates
Thanks for your design - I am considering them. PLease change the wording to :

```html
<!DOCTYPE html>
<html lang="en">
<head>
<meta charset="utf-8">
<title>Mira Corin – Business Card</title>
<link rel="stylesheet" href="https://fonts.googleapis.com/css2?family=Ubuntu:wght@400;700&family=Open+Sans:wght@400;600&family=Dancing+Script:wght@500&display=swap">
<style>
  :root {
    --backdrop: #e9ecef;
    --navy-light: #13283a;
    --navy: #0a1825;
    --navy-deep: #040d16;
    --turquoise: #1ea6c6;
    --turquoise-light: #3cc3de;
    --turquoise-dark: #137f9b;
    --green: #5cb85c;
    --text-light: #e8f1f5;
  }
  * { box-sizing: border-box; margin: 0; padding: 0; }
  html, body {
    width: 1200px;
    height: 900px;
    overflow: hidden;
    background: var(--backdrop);
  }
  .sheet {
    width: 1200px;
    height: 900px;
    display: flex;
    align-items: center;
    justify-content: center;
    gap: 40px;
  }
  .card {
    position: relative;
    width: 540px;
    height: 310px;
    border-radius: 22px;
    overflow: hidden;
    background: radial-gradient(ellipse at 35% 30%, var(--navy-light) 0%, var(--navy) 55%, var(--navy-deep) 100%);
    box-shadow: 0 10px 28px rgba(10, 24, 37, 0.28);
    color: var(--text-light);
  }

  /* ---------- Front ---------- */
  .brand {
    position: absolute;
    left: 44px;
    top: 48px;
    display: flex;
    flex-direction: column;
    align-items: flex-start;
    gap: 6px;
  }
  .brand-row {
    display: flex;
    align-items: center;
    gap: 10px;
  }
  .brand-dot {
    width: 22px;
    height: 22px;
    border-radius: 50%;
    background: var(--green);
  }
  .brand-name {
    font-family: "Ubuntu", sans-serif;
    font-weight: 700;
    font-size: 30px;
    line-height: 1.1;
    color: var(--turquoise);
    letter-spacing: 0.5px;
  }
  .brand-strap {
    font-family: "Dancing Script", cursive;
    font-size: 15px;
    color: var(--turquoise);
    padding-left: 32px;
  }
  .contacts {
    position: absolute;
    right: 32px;
    bottom: 100px;
    display: flex;
    align-items: stretch;
    gap: 18px;
    font-family: "Ubuntu", sans-serif;
    font-size: 12px;
    color: var(--turquoise);
  }
  .contact-column {
    display: flex;
    flex-direction: column;
    justify-content: center;
    gap: 10px;
  }
  .contact-divider {
    width: 1px;
    background: var(--turquoise);
    opacity: 0.8;
  }
  .contact-item {
    display: flex;
    align-items: center;
    gap: 8px;
    white-space: nowrap;
  }
  .contact-icon {
    width: 14px;
    height: 14px;
    flex: none;
  }
  .band-rule {
    position: absolute;
    left: 0;
    right: 0;
    bottom: 76px;
    height: 3px;
    background: var(--green);
  }
  .band {
    position: absolute;
    left: 0;
    right: 0;
    bottom: 0;
    height: 70px;
    background: linear-gradient(180deg, var(--turquoise-light) 0%, var(--turquoise) 45%, var(--turquoise-dark) 100%);
    display: flex;
    align-items: center;
    justify-content: center;
  }
  .band-strap {
    font-family: "Dancing Script", cursive;
    font-size: 22px;
    color: var(--navy);
  }

  /* ---------- Back ---------- */
  .pattern-field {
    position: absolute;
    inset: 0;
    background: radial-gradient(ellipse at 50% 45%, rgba(22, 48, 74, 0.55) 0%, rgba(10, 24, 37, 0) 75%);
  }
  .back-content {
    position: absolute;
    inset: 0;
    display: flex;
    flex-direction: column;
    align-items: center;
    justify-content: center;
    gap: 18px;
    padding: 0 30px;
  }
  .back-brand {
    display: flex;
    flex-direction: column;
    align-items: center;
    gap: 4px;
  }
  .back-brand .brand-name { font-size: 28px; }
  .back-brand .brand-strap { padding-left: 0; font-size: 14px; }
  .pitch {
    font-family: "Open Sans", sans-serif;
    font-size: 12px;
    line-height: 1.5;
    text-align: center;
    color: var(--text-light);
  }
  .pitch-link { color: var(--turquoise); }
</style>
</head>
<body>
<main class="sheet">

  <section class="card card-front" aria-label="Business card front">
    <div class="brand">
      <div class="brand-row">
        <span class="brand-dot"></span>
        <span class="brand-name">Mira Corin</span>
      </div>
      <span class="brand-strap">Re-Vitalising High Achievers</span>
    </div>

    <div class="contacts">
      <div class="contact-column">
        <div class="contact-item">
          <svg class="contact-icon" viewBox="0 0 16 16" aria-hidden="true">
            <path d="M4 1.5 L6.3 4.6 L5 6.2 C5.8 8 7.9 10.2 9.8 11 L11.4 9.7 L14.5 12 L13.2 14.3 C8 14.5 1.5 8 1.7 2.8 Z" fill="var(--turquoise)"/>
          </svg>
          <span>+44 7915 264318</span>
        </div>
        <div class="contact-item">
          <svg class="contact-icon" viewBox="0 0 16 16" aria-hidden="true">
            <rect x="1" y="3" width="14" height="10" rx="1.5" fill="var(--turquoise)"/>
            <path d="M1.8 4 L8 9 L14.2 4" fill="none" stroke="var(--navy)" stroke-width="1.4"/>
          </svg>
          <span>mira@corinvale.co.uk</span>
        </div>
      </div>
      <div class="contact-divider"></div>
      <div class="contact-column">
        <div class="contact-item">
          <svg class="contact-icon" viewBox="0 0 16 16" aria-hidden="true">
            <circle cx="8" cy="8" r="7" fill="var(--turquoise)"/>
          </svg>
          <span>miracorin</span>
        </div>
        <div class="contact-item">
          <svg class="contact-icon" viewBox="0 0 16 16" aria-hidden="true">
            <circle cx="8" cy="8" r="6.5" fill="none" stroke="var(--turquoise)" stroke-width="1.4"/>
            <ellipse cx="8" cy="8" rx="2.8" ry="6.5" fill="none" stroke="var(--turquoise)" stroke-width="1.2"/>
            <line x1="1.5" y1="8" x2="14.5" y2="8" stroke="var(--turquoise)" stroke-width="1.2"/>
          </svg>
          <span>www.corinvale.co.uk</span>
        </div>
      </div>
    </div>

    <div class="band-rule"></div>
    <div class="band">
      <span class="band-strap">Re-Vitalising High Achievers</span>
    </div>
  </section>

  <section class="card card-back" aria-label="Business card back">
    <div class="pattern-field" role="img" aria-label="Faint repeating leaf motif pattern across the dark navy background"></div>
    <div class="back-content">
      <div class="back-brand">
        <div class="brand-row">
          <span class="brand-dot"></span>
          <span class="brand-name">Mira Corin</span>
        </div>
        <span class="brand-strap">Re-Vitalising High Achievers</span>
      </div>
      <p class="pitch">
        Do you struggle to switch off?<br>
        Want to be healthier and feel fitter?<br>
        Want closer relationships?<br>
        More clarity over the direction you are headed?<br>
        I can help you do these things using integrated mind-body techniques.<br>
        Visit <span class="pitch-link">corinvale.co.uk</span> TODAY to apply for a FREE Breakthrough session.
      </p>
    </div>
  </section>

</main>
</body>
</html>
```